wooden jewelry - pearl necklaces

I sell wooden jeweler (rings and pearls) on markets, and so on. I also opened my business as a carpenter. The rings and a combination of wood and metal. The wood is special wood, not very common on Europe. I paint the rings afterwards. You can see some of the pictures on the pictures I uploaded. The pearls are made of the same kind of wood and colored in all kinds of colors. They are then assembled to bracelets. The jewelry is very individual and looks really cool and all kinds of people.

Target Market(s)

Young urban alternative with a sense of individuality

Contact Information for Business Card

Front:

Text:

„Kugelwerk“ (big)
„Malte Oswitz“ (smaler)

Back
„Holzschmuck
Herstellung von individuellem Holz- und Modeschmuck

Malte Oswitz
Tel: 015239460518
Lindgarbweg 9
83127 Altwiesen

malteoswitz@postfeld.de“

Font styles to use
Sans Serif

Requirements
Nice to have
• Nice to see a camel thorn tree on the background, this is a special wood and some of the rings are made out of this wood.

```html
<!DOCTYPE html>
<html lang="de">
<head>
<meta charset="utf-8">
<title>Kugelwerk – Visitenkarte</title>
<link href="https://fonts.googleapis.com/css2?family=Poppins:wght@500;700&family=Inter:wght@400;600;700&display=swap" rel="stylesheet">
<style>
  :root {
    --stage: #1a1a1c;
    --card-dark: #1c1a1d;
    --ink-dark: #1f1d20;
    --paper: #ffffff;
    --panel: rgba(255, 255, 255, 0.72);
    --bead-light: #d9c8ae;
    --bead-mid: #a57a52;
    --bead-deep: #3d2a22;
    --bead-accent: #6a2a2a;
  }
  * { margin: 0; padding: 0; box-sizing: border-box; }
  html, body {
    width: 1200px; height: 900px; overflow: hidden;
    background: var(--stage);
  }
  .stage { position: relative; width: 1200px; height: 900px; }

  .card {
    position: absolute;
    width: 490px; height: 280px;
    border-radius: 3px;
    overflow: hidden;
    box-shadow: 0 14px 30px rgba(0, 0, 0, 0.5);
  }

  /* Front */
  .card--front { left: 640px; top: 150px; }
  .card__beads {
    position: absolute; inset: 0;
    background:
      radial-gradient(circle at 20% 30%, var(--bead-light) 0, transparent 35%),
      radial-gradient(circle at 75% 70%, var(--bead-accent) 0, transparent 30%),
      radial-gradient(circle at 60% 20%, var(--bead-mid) 0, transparent 40%),
      linear-gradient(135deg, var(--bead-mid), var(--bead-deep) 55%, var(--bead-mid));
  }
  .card__panel {
    position: absolute; left: 52px; top: 40px; right: 52px; bottom: 40px;
    background: var(--panel);
  }
  .card__frames { position: absolute; inset: 0; }
  .card__brand {
    position: absolute; left: 0; right: 0; top: 100px;
    text-align: center;
    font-family: "Poppins", sans-serif;
    color: var(--ink-dark);
  }
  .card__title { font-size: 40px; font-weight: 700; line-height: 1; letter-spacing: 0.5px; }
  .card__owner { font-size: 20px; font-weight: 500; margin-top: 6px; }

  /* Back */
  .card--back {
    left: 80px; top: 470px;
    background: var(--card-dark);
    color: var(--paper);
    font-family: "Inter", sans-serif;
    text-align: center;
    padding-top: 46px;
  }
  .back__name { font-size: 28px; font-weight: 700; }
  .back__rule { width: 150px; height: 2px; background: var(--paper); margin: 14px auto; }
  .back__trade { font-size: 18px; font-weight: 700; }
  .back__tagline { font-size: 13px; margin-top: 3px; }
  .back__contact { font-size: 13px; line-height: 1.4; }
</style>
</head>
<body>
<main class="stage">

  <section class="card card--front">
    <div class="card__beads" role="img" aria-label="Foto bunter Holzperlen in Creme-, Braun- und Rottönen"></div>
    <div class="card__panel"></div>
    <svg class="card__frames" width="490" height="280" viewBox="0 0 490 280" fill="none" stroke="#ffffff" stroke-width="2.5">
      <rect x="42" y="30" width="406" height="220"/>
      <rect x="30" y="42" width="418" height="200"/>
      <rect x="56" y="22" width="378" height="236"/>
    </svg>
    <div class="card__brand">
      <div class="card__title">Kugelwerk</div>
      <div class="card__owner">Malte Oswitz</div>
    </div>
  </section>

  <section class="card card--back">
    <div class="back__name">Malte Oswitz</div>
    <div class="back__rule"></div>
    <div class="back__trade">Holzschmuck</div>
    <div class="back__tagline">Herstellung von individuellem Holz- und Modeschmuck</div>
    <div class="back__rule"></div>
    <div class="back__contact">
      01 523 946 0518<br>
      malteoswitz@postfeld.de<br>
      Lindgarbweg 9, 83127 Altwiesen
    </div>
  </section>

</main>
</body>
</html>
```